Hvac and insulation company needs good looking business card design

We are hvac and insulation company and looking for a new business cards that look to today standards designs

Target Market(s)

homeowners

Industry/Entity Type

Hvac

Contact Information for Business Card

Name: Dorian Velkova
Home comfort consultant
address: 4827 Marrow Ridge Rd #215 Oakland, CA 94611
office: 888-317-5069
cell: 510-642-1388
Lic.# 458127
Email: dorian@quarry-hvac.com
Web: quarry-hvac.com

Requirements
Must have
• clean and sleek look
Nice to have
• simple with a clean look
Should not have
• to busy business card

```html
<!DOCTYPE html>
<html lang="en">
<head>
<meta charset="utf-8">
<title>Quarry Home Comfort – Business Card</title>
<link rel="stylesheet" href="https://fonts.googleapis.com/css2?family=Source+Sans+3:wght@400;600;700&display=swap">
<style>
  :root {
    --backdrop: #b5b5b5;
    --card-white: #ffffff;
    --card-grey: #606060;
    --brand-orange: #ff6a00;
    --ink: #141414;
    --ink-soft: #555555;
    --ink-contact: #2a2a2a;
  }
  * { margin: 0; padding: 0; box-sizing: border-box; }
  html, body { width: 1200px; height: 1200px; overflow: hidden; }
  body {
    background: var(--backdrop);
    font-family: "Source Sans 3", sans-serif;
    position: relative;
  }
  .card-shapes { position: absolute; inset: 0; }
  .front, .back { position: absolute; inset: 0; }

  .brand-mark-square { display: block; background: var(--brand-orange); flex: none; }
  .brand-name { color: var(--brand-orange); font-weight: 700; line-height: 1; }

  .brand-front {
    position: absolute; left: 604px; top: 170px; height: 70px;
    display: flex; align-items: center; gap: 40px;
  }
  .brand-front .brand-mark-square { width: 58px; height: 58px; }
  .brand-front .brand-name { font-size: 60px; margin-top: -12px; }

  .person { position: absolute; left: 276px; top: 334px; }
  .person-name { font-size: 36px; font-weight: 600; color: var(--ink); line-height: 1.1; }
  .person-title { font-size: 23px; font-weight: 400; color: var(--ink-soft); line-height: 1.2; margin-top: 2px; }

  .contact { position: absolute; left: 606px; top: 305px; font-size: 19.5px; color: var(--ink-contact); }
  .contact-row { display: flex; line-height: 24.5px; }
  .contact-label { width: 35px; }
  .contact-value { padding-left: 4px; }
  .contact-indent { padding-left: 10px; }
  .gap-sm { margin-top: 15px; }
  .gap-md { margin-top: 10.5px; }
  .license { position: absolute; left: 693px; top: 497px; font-size: 24px; color: var(--ink-contact); }

  .brand-back {
    position: absolute; left: 320px; top: 770px; height: 120px;
    display: flex; align-items: center; gap: 46px;
  }
  .brand-back .brand-mark-square { width: 112px; height: 112px; }
  .brand-back .brand-name { font-size: 112px; margin-top: -22px; }

  .web-back {
    position: absolute; left: 0; width: 1200px; top: 1008px;
    text-align: center; color: #ffffff; font-size: 23px; letter-spacing: 0.72em;
    padding-left: 0.72em;
  }
</style>
</head>
<body>
  <svg class="card-shapes" width="1200" height="1200" viewBox="0 0 1200 1200" aria-hidden="true">
    <defs>
      <clipPath id="front-outline">
        <path d="M216,134 H943 A38,38 0 0 1 981,172 V596 H254 A38,38 0 0 1 216,558 Z"/>
      </clipPath>
    </defs>
    <g clip-path="url(#front-outline)">
      <rect x="216" y="134" width="765" height="462" fill="var(--card-white)"/>
      <path class="front-band" d="M216,548 L732,564 L864,545 L981,545 V596 H216 Z" fill="var(--card-grey)"/>
      <path class="front-accent" d="M296,544 L840,544 L732,558 Z" fill="var(--brand-orange)"/>
    </g>
    <path class="back-card" d="M254,607 H981 V1031 A38,38 0 0 1 943,1069 H216 V645 A38,38 0 0 1 254,607 Z" fill="var(--card-grey)"/>
  </svg>

  <section class="front">
    <div class="brand-front">
      <span class="brand-mark-square"></span>
      <span class="brand-name">quarry</span>
    </div>

    <div class="person">
      <div class="person-name">Dorian Velkova</div>
      <div class="person-title">Home comfort consultant</div>
    </div>

    <div class="contact">
      <div class="contact-row"><span class="contact-label">A</span><span class="contact-value">: 4827 Marrow Ridge Rd #215 Alderbrook</span></div>
      <div class="contact-row"><span class="contact-label"></span><span class="contact-value contact-indent">CA 94790</span></div>
      <div class="contact-row gap-sm"><span class="contact-label">P</span><span class="contact-value">: 888-317-5069</span></div>
      <div class="contact-row"><span class="contact-label">C</span><span class="contact-value">: 510-642-1388</span></div>
      <div class="contact-row"><span class="contact-label">E</span><span class="contact-value">: dorian@quarry-hvac.com</span></div>
      <div class="contact-row gap-md"><span class="contact-label">W</span><span class="contact-value">: www.quarry-hvac.com</span></div>
    </div>

    <div class="license">Lic.# 458127</div>
  </section>

  <section class="back">
    <div class="brand-back">
      <span class="brand-mark-square"></span>
      <span class="brand-name">quarry</span>
    </div>
    <div class="web-back">www.quarry-hvac.com</div>
  </section>
</body>
</html>
```